Technology Solutions Provider

Let’s design a business card that will be as simple and bold at the same time. Name, email address, website & phone number.

Target Market(s)

Small to Medium Size Business

Industry/Entity Type

It Professional

Contact Information for Business Card

Name, email, website, phone numbers

Font styles to use
Sans Serif

Colors
ec1f27
f04a50
dddddd
919191
000000
ffffff

Requirements
Must have
• Clean simple look using my existing logo. I just need to the basic contact information on this card.
Nice to have
• Im considering the square size card versus the standard size business card.
Should not have
• No Mailing Address, no list of services.

```html
<!DOCTYPE html>
<html lang="en">
<head>
<meta charset="utf-8">
<title>Apex Linkworks – Square Business Cards</title>
<link href="https://fonts.googleapis.com/css2?family=Open+Sans:wght@400;600&family=Lato:wght@700&display=swap" rel="stylesheet">
<style>
  :root {
    --brand-red: #ec1f27;
    --brand-red-soft: #f04a50;
    --light-grey: #dddddd;
    --mid-grey: #919191;
    --ink: #000000;
    --paper: #ffffff;
    --backdrop: #3b3b3b;
  }
  * { box-sizing: border-box; margin: 0; padding: 0; }
  html, body {
    width: 1200px; height: 800px; overflow: hidden;
    background: var(--backdrop);
    font-family: "Open Sans", sans-serif;
  }
  .card-sheet {
    position: relative; width: 1200px; height: 800px;
    display: flex; align-items: center; justify-content: center; gap: 60px;
  }
  .card {
    width: 460px; height: 460px; position: relative;
  }
  /* Front */
  .card--front {
    background: var(--brand-red);
    border: 8px solid var(--paper);
    color: var(--paper);
  }
  .card--front .wordmark {
    position: absolute; top: 170px; left: 0; right: 0; text-align: center;
    font-size: 38px; font-weight: 400; color: var(--paper); letter-spacing: 0.5px;
  }
  .card--front .website {
    position: absolute; bottom: 70px; left: 0; right: 0; text-align: center;
    font-size: 16px; letter-spacing: 0.5px;
  }
  /* Back */
  .card--back {
    background: var(--paper);
    border: 10px solid var(--brand-red);
    color: var(--ink);
  }
  .card--back .wordmark {
    position: absolute; top: 70px; left: 0; right: 0; text-align: center;
    font-size: 36px; font-weight: 400; color: var(--brand-red); letter-spacing: 0.5px;
  }
  .holder {
    position: absolute; top: 184px; left: 0; right: 0; text-align: center;
  }
  .holder__name {
    font-family: "Lato", sans-serif; font-weight: 700;
    font-size: 28px; color: var(--brand-red);
  }
  .holder__title { font-size: 16px; margin-top: 2px; }
  .divider {
    position: absolute; top: 272px; left: 34px; right: 34px;
    height: 1.5px; background: var(--brand-red);
  }
  .contact {
    position: absolute; left: 24px; right: 24px; font-size: 15px;
    display: flex; align-items: center; gap: 6px;
  }
  .contact svg { width: 14px; height: 14px; flex: none; }
  .contact--phone { top: 300px; justify-content: center; }
  .contact-row {
    position: absolute; top: 336px; left: 20px; right: 20px;
    display: flex; justify-content: space-between; font-size: 14.5px;
  }
  .contact-row .contact { position: static; }
</style>
</head>
<body>
<main class="card-sheet">
  <section class="card card--front" aria-label="Card front">
    <div class="wordmark">Apex Linkworks</div>
    <div class="website">www.apexlinkworks.com</div>
  </section>

  <section class="card card--back" aria-label="Card back">
    <div class="wordmark">Apex Linkworks</div>
    <div class="holder">
      <div class="holder__name">Daniel Hartley</div>
      <div class="holder__title">Manager</div>
    </div>
    <div class="divider"></div>
    <div class="contact contact--phone">
      <svg viewBox="0 0 24 24" aria-hidden="true"><path fill="var(--brand-red)" d="M6.6 10.8c1.4 2.8 3.8 5.1 6.6 6.6l2.2-2.2c.3-.3.7-.4 1-.2 1.1.4 2.3.6 3.6.6.6 0 1 .4 1 1V20c0 .6-.4 1-1 1C10.6 21 3 13.4 3 4c0-.6.4-1 1-1h3.5c.6 0 1 .4 1 1 0 1.3.2 2.5.6 3.6.1.3 0 .7-.2 1L6.6 10.8z"/></svg>
      <span>512 555 0147</span>
    </div>
    <div class="contact-row">
      <div class="contact">
        <svg viewBox="0 0 24 24" aria-hidden="true"><rect x="2" y="5" width="20" height="14" fill="var(--brand-red)"/><path d="M2 5l10 8 10-8" fill="none" stroke="#fff" stroke-width="1.6"/></svg>
        <span>info@apexlinkworks.com</span>
      </div>
      <div class="contact">
        <svg viewBox="0 0 24 24" aria-hidden="true"><circle cx="12" cy="12" r="10" fill="var(--brand-red)"/><path d="M2 12h20M12 2c3 3 3 17 0 20M12 2c-3 3-3 17 0 20" fill="none" stroke="#fff" stroke-width="1.3"/></svg>
        <span>www.apexlinkworks.com</span>
      </div>
    </div>
  </section>
</main>
</body>
</html>
```